Lantern Word Search Activity Book Series

The design will be used across a series (3) of Word Search puzzle books on the Bibile: The Amber Scrolls Volume 1, The Book Of Marrow Volume 1, and the Book Of Tindle Volume 1. The design can be the same on all three books the titles will of course just need to be different (open to creative suggestions here.) Some ideas for the titles of each include: “Lantern Word Search Large Print Puzzles For Adults and Kids Volume 1,” and/or “Book Of Marrow Word Search Large Print Volume 1” etc.

Target Market(s)

Adults middle age and older and kids. The three books might also be used for a biblical word association study aid. This will be a printed book targeting those that have an interest in printed activity books and biblical study material and may want an alternative to games on electronic devices like Velotabs.

Industry/Entity Type

Games

Font styles to use
Serif
Script

Colors

Designer to choose colors to be used in the design.

Requirements
Must have
• Most of the printed puzzle and activity books that are available today, with the exception of those published by The Harlow Dispatch are very dry would like to see something unique and eye catching with a clear title.
Nice to have
• Would be nice to perhaps have a bible somewhere in the cover design. Possible idea might be a silhouette of a person looking in to or reading the Bible. I've attached some designs from current puzzle books that have caught my attention. Design might incorporate something biblical but it doesn't necessarily have to. Would like to see the use of some color in the design.

```html
<!DOCTYPE html>
<html lang="en">
<head>
<meta charset="utf-8">
<title>The Amber Scrolls – Volume 1</title>
<link href="https://fonts.googleapis.com/css2?family=Berkshire+Swash&family=Great+Vibes&display=swap" rel="stylesheet">
<style>
  :root {
    --rose-light: #f4d9df;
    --rose-mid: #e7a3b6;
    --rose-deep: #b9557e;
    --cream: #f3e6cf;
    --band: rgba(128, 52, 82, 0.55);
    --band-edge: rgba(250, 225, 232, 0.55);
    --title-fill: #fbf1e6;
    --title-ink: #5a1730;
    --script-ink: #4a1026;
    --book-cover: #c98b4a;
    --book-page: #fff8ec;
  }
  * { margin: 0; padding: 0; box-sizing: border-box; }
  html, body { width: 841px; height: 1200px; overflow: hidden; }
  .cover {
    position: relative;
    width: 841px;
    height: 1200px;
    overflow: hidden;
  }
  .rose-field {
    position: absolute;
    inset: 0;
    background:
      radial-gradient(circle at 15% 10%, var(--cream) 0, transparent 22%),
      radial-gradient(circle at 80% 30%, var(--rose-deep) 0, transparent 25%),
      radial-gradient(circle at 30% 60%, var(--rose-mid) 0, transparent 28%),
      radial-gradient(circle at 75% 75%, var(--cream) 0, transparent 22%),
      radial-gradient(circle at 15% 90%, var(--rose-deep) 0, transparent 24%),
      linear-gradient(160deg, var(--rose-light), var(--rose-mid) 50%, var(--rose-deep));
  }
  .title-band {
    position: absolute;
    left: 0;
    top: 174px;
    width: 100%;
    height: 353px;
    background: var(--band);
    border-top: 14px solid var(--band-edge);
    border-bottom: 14px solid var(--band-edge);
    text-align: center;
  }
  .book-title {
    margin-top: 48px;
    font-family: "Berkshire Swash", serif;
    font-weight: 400;
    font-size: 96px;
    line-height: 1.1;
    color: var(--title-fill);
    -webkit-text-stroke: 2px var(--title-ink);
    text-shadow: 3px 3px 0 var(--title-ink);
  }
  .volume {
    display: flex;
    align-items: center;
    justify-content: center;
    gap: 18px;
    margin-top: 2px;
    font-family: "Great Vibes", cursive;
    font-size: 50px;
    color: var(--script-ink);
  }
  .volume::before, .volume::after {
    content: "";
    width: 46px;
    height: 2px;
    background: var(--title-fill);
  }
  .book-icon {
    display: block;
    margin: 6px auto 0;
  }
</style>
</head>
<body>
  <main class="cover">
    <div class="rose-field" role="img" aria-label="Dense field of pink, cream and mauve roses covering the whole cover"></div>
    <header class="title-band">
      <h1 class="book-title">The Amber Scrolls</h1>
      <p class="volume">Volume 1</p>
      <svg class="book-icon" width="92" height="74" viewBox="0 0 92 74" aria-hidden="true">
        <rect x="2" y="4" width="88" height="68" rx="3" fill="var(--book-cover)"/>
        <path d="M8 8 H44 V66 H8 Z" fill="var(--book-page)"/>
        <path d="M48 8 H84 V66 H48 Z" fill="var(--book-page)"/>
        <line x1="46" y1="6" x2="46" y2="70" stroke="#8a5a2b" stroke-width="3"/>
      </svg>
    </header>
  </main>
</body>
</html>
```